Internal Web Pages for Metrivane Labs

I need internal web pages (Why Metrivane Labs?, What We Offer, Blog, Testimonials) that match the design of the homepage. These do not need to be as long or in-depth as the landing page (provided for reference) but I will need three, maybe four, total pages (I'll select the max number of pages for now, but these will all be simple and short pages). Also attached is our new logo design for the company.

They are to essentially be:
Why Metrivane Labs? - An About Us and Why Choose Us page rolled into one.
What We Offer - A Services type page
Blog - self-explanatory
Testimonials - Customer Reviews and Use Cases

Also, maybe a very simple "Contact Us" page as well.

Target Market(s)

Business professionals that work with data analytics teams

Industry/Entity Type

Data Science

Number of Pages Required

5+ page

Requirements
Must have
• It must match the original design in theme and colors.
Nice to have
• Simple pages that show continuity that flows from the original landing page.
Should not have
• Can not be a different design that does not match the landing page.

```html
<!DOCTYPE html>
<html lang="en">
<head>
<meta charset="utf-8">
<title>Metrivane Labs — Our Services</title>
<link href="https://fonts.googleapis.com/css2?family=Poppins:wght@300;400;500&family=Hind:wght@300;400;500&family=Montserrat:wght@600&family=Roboto:wght@500;700&display=swap" rel="stylesheet">
<style>
:root{
  --ink:#1d1d22;
  --muted:#3a3a44;
  --brand:#4a54e1;
  --brand-light:#7a9bef;
  --orange:#f08300;
  --hero:#141418;
  --band:#5a62e6;
  --footer:#170040;
  --footer-base:#140236;
  --white:#ffffff;
}
*{margin:0;padding:0;box-sizing:border-box}
html,body{width:843px;height:1200px;overflow:hidden;background:var(--white)}
body{position:relative;font-family:"Hind",sans-serif;color:var(--ink)}
.abs{position:absolute}

/* header */
.site-header{position:absolute;left:0;top:0;width:843px;height:61px;background:var(--white)}
.brand{position:absolute;left:66px;top:13px;display:flex;align-items:center;gap:6px;font-family:"Poppins",sans-serif;font-weight:300;font-size:25px;color:var(--brand);letter-spacing:.2px}
.brand-mark{width:16px;height:16px;background:var(--brand);border-radius:50%}
.nav a{position:absolute;top:21px;font-family:"Poppins",sans-serif;font-weight:300;font-size:12.5px;color:#333;text-decoration:none}
.nav a.active{color:var(--brand-light)}
.btn-start{position:absolute;left:685px;top:16px;width:93px;height:27px;background:var(--orange);color:#fff;font-family:"Roboto",sans-serif;font-weight:700;font-size:9.5px;letter-spacing:.4px;display:flex;align-items:center;justify-content:center;box-shadow:0 3px 6px rgba(0,0,0,.15)}

/* hero */
.hero{position:absolute;left:0;top:61px;width:843px;height:260px}
.hero-title{position:absolute;left:59px;top:127px;font-family:"Poppins",sans-serif;font-weight:400;font-size:26px;color:#fff}
.hero-sub{position:absolute;left:60px;top:164px;font-size:12.2px;color:#fff;font-weight:400}

/* offer */
.offer-title{position:absolute;left:0;width:843px;top:384px;text-align:center;font-family:"Poppins",sans-serif;font-weight:300;font-size:27px;color:var(--ink)}
.offer-rule{position:absolute;left:371px;top:422px;width:101px;height:1.5px;background:var(--brand)}
.offer-sub{position:absolute;left:0;width:843px;top:433px;text-align:center;font-size:10.8px;font-weight:300;color:var(--muted)}
.feature{position:absolute;width:190px}
.feature h3{font-family:"Montserrat",sans-serif;font-weight:600;font-size:12.6px;color:#2b2b33;margin-bottom:5px}
.feature p{font-size:10.6px;line-height:14.7px;font-weight:300;color:var(--muted)}
.feature.left{text-align:right;left:78px}
.feature.right{left:574px}
.feature-icon{position:absolute;width:34px;height:34px}
.offer-art{position:absolute;left:338px;top:505px;width:172px;height:170px;border-radius:10px;background:linear-gradient(135deg,#c9d6fb 0%,#8ea8f1 50%,#5a62e6 100%)}

/* footer */
.site-footer{position:absolute;left:0;top:795px;width:843px;height:305px;background:var(--footer);color:#fff}
.footer-base{position:absolute;left:0;top:1099px;width:843px;height:101px;background:var(--footer-base)}
.f-brand{position:absolute;left:101px;top:872px;display:flex;align-items:center;gap:6px;font-family:"Poppins",sans-serif;font-weight:300;font-size:23px;color:#fff}
.f-brand .brand-mark{background:var(--brand-light);width:15px;height:15px}
.f-about{position:absolute;left:101px;top:913px;width:200px;font-size:11.3px;line-height:15.7px;color:#fff}
.social{position:absolute;top:1005px;width:25px;height:25px;border:1.2px solid #fff;border-radius:50%}
.f-head{position:absolute;font-family:"Roboto",sans-serif;font-weight:700;font-size:12.8px;color:#fff;letter-spacing:.2px}
.c-item{position:absolute;left:364px;font-family:"Roboto",sans-serif;font-weight:500;font-size:11px;line-height:15px;letter-spacing:.6px;color:#fff}
.c-icon{position:absolute;left:337px;width:14px;height:14px}
.sign-text{position:absolute;left:530px;top:903px;width:230px;font-size:10.3px;line-height:16.5px;color:#fff;white-space:nowrap}
.email-field{position:absolute;left:529px;top:947px;width:214px;height:29px;background:#fff;border-radius:2px;font-size:10.3px;color:#666;padding:8px 0 0 13px}
.btn-sub{position:absolute;left:529px;top:987px;width:90px;height:28px;background:var(--orange);color:#fff;font-family:"Roboto",sans-serif;font-weight:700;font-size:9.8px;display:flex;align-items:center;justify-content:center}
.copyright{position:absolute;left:0;width:843px;top:1143px;text-align:center;font-size:11.3px;font-weight:500;color:#fff}
</style>
</head>
<body>

<header class="site-header">
  <div class="brand"><span class="brand-mark"></span>MetrivaneLabs</div>
  <nav class="nav">
    <a style="left:328px">Home</a>
    <a style="left:386px">About us</a>
    <a class="active" style="left:462px">Our Service</a>
    <a style="left:553px">Blog</a>
    <a style="left:601px">Contact</a>
  </nav>
  <div class="btn-start">GET STARTED</div>
</header>

<section class="hero">
  <svg width="843" height="260" viewBox="0 0 843 260" class="abs" style="left:0;top:0">
    <defs>
      <linearGradient id="heroPhoto" x1="0" y1="0" x2="1" y2="0">
        <stop offset="0" stop-color="#141418"/>
        <stop offset=".4" stop-color="#2a2444"/>
        <stop offset=".6" stop-color="#4a4a9a"/>
        <stop offset="1" stop-color="#1a2a55"/>
      </linearGradient>
    </defs>
    <polygon points="0,0 843,0 843,186 291,254 0,177" fill="var(--hero)"/>
    <path d="M80,195 L291,254 L843,176 L843,184 L291,260 Z" fill="var(--band)"/>
    <g role="img" aria-label="Photo of a hand touching a glowing compliance checklist surrounded by connected icons">
      <polygon points="330,0 843,0 843,176 560,216 330,210" fill="url(#heroPhoto)" opacity=".9"/>
    </g>
  </svg>
  <h1 class="hero-title">Our Servies</h1>
  <p class="hero-sub">Advanced Metrivane Labs Strategies Services</p>
</section>

<h2 class="offer-title">What we offer</h2>
<div class="offer-rule"></div>
<p class="offer-sub">Sed ut perspiciatis unde omnis iste natus sit.</p>

<div class="feature left" style="top:480px"><h3>Neque porro quisquam</h3><p>Sed ut perspiciatis unde omnis iste voluptatem accusantium doloremque laudantium, totam rem.</p></div>
<div class="feature left" style="top:565px"><h3>Neque porro quisquam</h3><p>Sed ut perspiciatis unde omnis iste voluptatem accusantium doloremque laudantium, totam rem.</p></div>
<div class="feature left" style="top:658px"><h3>Neque porro quisquam</h3><p>Sed ut perspiciatis unde omnis iste voluptatem accusantium doloremque laudantium, totam rem.</p></div>
<div class="feature right" style="top:480px"><h3>Neque porro quisquam</h3><p>Sed ut perspiciatis unde omnis iste voluptatem accusantium doloremque laudantium, totam rem.</p></div>
<div class="feature right" style="top:565px"><h3>Neque porro quisquam</h3><p>Sed ut perspiciatis unde omnis iste voluptatem accusantium doloremque laudantium, totam rem.</p></div>
<div class="feature right" style="top:658px"><h3>Neque porro quisquam</h3><p>Sed ut perspiciatis unde omnis iste voluptatem accusantium doloremque laudantium, totam rem.</p></div>

<svg class="feature-icon" style="left:283px;top:481px" viewBox="0 0 34 34" fill="none" stroke="#2a2a5a" stroke-width="1.2">
  <path d="M2 1h18l7 7v24H2z"/><circle cx="10" cy="11" r="5" stroke="var(--orange)"/><path d="M8 30v-6h4v6M14 30v-9h4v9M20 30v-12h4v12"/>
</svg>
<svg class="feature-icon" style="left:281px;top:569px" viewBox="0 0 34 34" fill="none" stroke="#2a2a5a" stroke-width="1.2">
  <rect x="2" y="10" width="20" height="14"/><path d="M8 28h8M12 24v4"/><circle cx="17" cy="18" r="6" stroke="var(--orange)"/><rect x="24" y="2" width="8" height="6" stroke="var(--orange)"/><path d="M28 20v12M31 22v10" stroke="var(--orange)"/>
</svg>
<svg class="feature-icon" style="left:284px;top:662px" viewBox="0 0 34 34" fill="none" stroke="#2a2a5a" stroke-width="1.2">
  <rect x="2" y="2" width="26" height="30"/><path d="M6 8h12M6 12h10" stroke="var(--orange)"/><path d="M5 26l6-6 5 4 8-8"/><circle cx="27" cy="8" r="5"/>
</svg>
<svg class="feature-icon" style="left:532px;top:481px" viewBox="0 0 34 34" fill="none" stroke="#2a2a5a" stroke-width="1.2">
  <circle cx="12" cy="12" r="9"/><circle cx="12" cy="12" r="5" stroke="var(--orange)"/><path d="M19 19l10 10"/><path d="M24 2l6-1-1 6" stroke="var(--orange)"/>
</svg>
<svg class="feature-icon" style="left:532px;top:569px" viewBox="0 0 34 34" fill="none" stroke="#2a2a5a" stroke-width="1.2">
  <rect x="2" y="8" width="26" height="18"/><circle cx="9" cy="17" r="5" stroke="var(--orange)"/><path d="M18 14v-4M22 14v-6M26 14v-8" stroke="var(--orange)"/><path d="M30 12v20M27 15l3-3 3 3"/>
</svg>
<svg class="feature-icon" style="left:534px;top:662px" viewBox="0 0 34 34" fill="none" stroke="#2a2a5a" stroke-width="1.2">
  <rect x="2" y="2" width="26" height="28"/><path d="M6 8h4M6 14h4M6 20h4M13 8h11M13 14h11M13 20h8"/><circle cx="27" cy="25" r="6" stroke="var(--orange)"/><path d="M24 25l2 2 4-4" stroke="var(--orange)"/>
</svg>

<div class="offer-art" role="img" aria-label="Illustration of a growth graphic with dots, a rising line and bars in blue tones"></div>

<footer class="site-footer"></footer>
<div class="footer-base"></div>

<div class="f-brand"><span class="brand-mark"></span>MetrivaneLabs</div>
<p class="f-about">Sed ut perspiciatis unde omnis iste natus error sit voluptatem accusantium dolorque laudantium, totam rem aperiam, eaque ipsa quae ab illo inventore veritatis et quasi</p>
<span class="social" style="left:101px"></span>
<span class="social" style="left:130px"></span>
<span class="social" style="left:159px"></span>
<span class="social" style="left:188px"></span>

<h4 class="f-head" style="left:337px;top:876px">CONTACT US</h4>
<svg class="c-icon" style="top:907px" viewBox="0 0 14 14" fill="none" stroke="#fff" stroke-width="1"><path d="M7 13C3 8 2 6 2 5a5 5 0 0 1 10 0c0 1-1 3-5 8z"/><circle cx="7" cy="5" r="1.8"/></svg>
<p class="c-item" style="top:903px">Metrivane Labs<br>250 ipsam voluptatem<br>quia voluptas</p>
<svg class="c-icon" style="top:960px" viewBox="0 0 14 14" fill="none" stroke="#fff" stroke-width="1"><path d="M3 1l3 3-2 2c1 2 2 3 4 4l2-2 3 3-2 2C6 13 1 8 1 3z"/></svg>
<p class="c-item" style="top:961px">Phone :<br><span style="display:block;margin-top:2px">555-0140-2290</span></p>
<svg class="c-icon" style="top:1005px" viewBox="0 0 14 14" fill="none" stroke="#fff" stroke-width="1"><rect x="1" y="3" width="12" height="8"/><path d="M1 3l6 5 6-5"/></svg>
<p class="c-item" style="top:1005px">Email :<br>hello@metrivanelabs.com</p>

<h4 class="f-head" style="left:530px;top:874px">SIGN UP TO RECEIVE EMAIL</h4>
<p class="sign-text">Excepteur sint occaecat cupidatat non proi-<br>dent, sunt in culpa qui Nemo enim ipsam vo-</p>
<div class="email-field">Enter Email</div>
<div class="btn-sub">SUBSCRIBE</div>

<p class="copyright">Copyright © Metrivane Labs 2021. All rights reserved. | Privacy Policy</p>

</body>
</html>
```